Increasing performance of Security Operations Centers

Stellavant builds Security Operations Centers (SOC) that enable Pinnacle 1000 clients to be proactive and predictive in the way they secure their people and facilities. The methods involve automating threat detection, streamlining workflows, and outsourcing the most appropriate tasks. The outcomes are a reduction in total incidents and faster response times with fewer resources so clients can focus on their core business.
We're looking for 2 slides to replace the attached PPT. The first slide would be broken into each of the 8 capabilities when presenting: i.e. starting with "Reduce incidents..." on the first slide, building on with "Better direct..." on the second and continuing around clockwise. I'm looking for a more compelling way to present the capabilities and am not wedded to the way it is laid out now.
Also attached is our brand book for color and font values to comply with.

I will extend the deadline to 3/28 as soon as I figure out how.

```html
<!DOCTYPE html>
<html lang="en">
<head>
<meta charset="utf-8">
<title>SOC Performance Improvement Objectives – Stellavant</title>
<link href="https://fonts.googleapis.com/css2?family=Arimo:wght@400;700&display=swap" rel="stylesheet">
<style>
  :root {
    --canvas: #bdbdbf;
    --paper: #ffffff;
    --navy: #0b3d61;
    --ink: #0f2b4a;
    --signal-red: #c1312b;
    --slate: #8d99ad;
    --hairline: #eeeff2;
    --white: #ffffff;
  }
  * { margin: 0; padding: 0; box-sizing: border-box; }
  html, body {
    width: 960px; height: 1200px; overflow: hidden;
    background: var(--canvas);
    font-family: "Arimo", Arial, sans-serif;
  }
  .deck { position: relative; width: 960px; height: 1200px; }
  .slide {
    position: absolute; left: 118.4px; width: 723.2px; height: 541.6px;
    display: block; background: var(--paper);
  }
  .slide--overview { top: 52px; }
  .slide--summary { top: 612px; }
  .band { fill: var(--navy); }
  .hairline { stroke: var(--hairline); stroke-width: 1; }
  .slide-title { fill: var(--white); font-size: 38px; font-weight: 400; }
  .brand-name { fill: var(--white); font-size: 38px; font-weight: 400; }
  .tile--navy { fill: var(--navy); }
  .tile--ink { fill: var(--ink); }
  .tile--red { fill: var(--signal-red); }
  .tile--slate { fill: var(--slate); }
  .tile-text { fill: var(--white); font-size: 19px; text-anchor: middle; }
  .hub--ink { fill: var(--ink); }
  .hub--navy { fill: var(--navy); }
  .headline { font-size: 28px; font-weight: 700; text-anchor: middle; fill: var(--navy); }
  .headline .accent { fill: var(--signal-red); }
  .hub-text { fill: var(--white); font-size: 26px; font-weight: 700; text-anchor: middle; }
</style>
</head>
<body>
<main class="deck">

  <!-- Slide 1: capability overview -->
  <svg class="slide slide--overview" viewBox="0 0 904 677" xmlns="http://www.w3.org/2000/svg" aria-label="SOC Performance Improvement Objectives overview">
    <line class="hairline" x1="0" y1="321" x2="904" y2="321"/>
    <polygon class="band" points="0,0 388,0 412,27 904,27 904,97 0,97"/>
    <text class="slide-title" x="44" y="80">SOC Performance Improvement Objectives…</text>

    <circle class="hub--ink" cx="452" cy="367" r="110"/>

    <rect class="tile--slate" x="339" y="110" width="215" height="117" rx="4"/>
    <text class="tile-text"><tspan x="446.5" y="149">Reduce  incidents,</tspan><tspan x="446.5" y="173">respond faster,</tspan><tspan x="446.5" y="197">with fewer resources</tspan></text>

    <rect class="tile--red" x="602" y="168" width="215" height="117" rx="4"/>
    <text class="tile-text"><tspan x="709.5" y="189">Better direct your</tspan><tspan x="709.5" y="211">security/safety</tspan><tspan x="709.5" y="232">personnel to situations</tspan><tspan x="709.5" y="254">where they are</tspan><tspan x="709.5" y="275">needed most.</tspan></text>

    <rect class="tile--ink" x="602" y="306" width="215" height="117" rx="4"/>
    <text class="tile-text"><tspan x="709.5" y="334">Free up time for</tspan><tspan x="709.5" y="358">more engagement,</tspan><tspan x="709.5" y="382">deterrence, and</tspan><tspan x="709.5" y="406">investigations</tspan></text>

    <rect class="tile--navy" x="602" y="443" width="215" height="117" rx="4"/>
    <text class="tile-text"><tspan x="709.5" y="483">Lessen your</tspan><tspan x="709.5" y="507">management</tspan><tspan x="709.5" y="531">burden</tspan></text>

    <rect class="tile--slate" x="339" y="507" width="215" height="117" rx="4"/>
    <text class="tile-text"><tspan x="446.5" y="528">Increase your</tspan><tspan x="446.5" y="549">installed systems</tspan><tspan x="446.5" y="571">protective usefulness</tspan><tspan x="446.5" y="592">&amp; adaptability to</tspan><tspan x="446.5" y="614">new threats</tspan></text>

    <rect class="tile--red" x="86" y="443" width="215" height="117" rx="4"/>
    <text class="tile-text"><tspan x="193.5" y="483">Automate threat</tspan><tspan x="193.5" y="507">detection,</tspan><tspan x="193.5" y="531">streamline workflows</tspan></text>

    <rect class="tile--ink" x="86" y="306" width="215" height="117" rx="4"/>
    <text class="tile-text"><tspan x="193.5" y="346">Outsource Key</tspan><tspan x="193.5" y="370">or Non-Core</tspan><tspan x="193.5" y="394">Functions</tspan></text>

    <rect class="tile--navy" x="86" y="168" width="215" height="117" rx="4"/>
    <text class="tile-text"><tspan x="193.5" y="220">Reduce</tspan><tspan x="193.5" y="244">Total Cost</tspan></text>

    <polygon class="band" points="617,617 904,617 904,677 0,677 0,660 580,660"/>
    <text class="brand-name" x="864" y="661" text-anchor="end">Stellavant</text>
  </svg>

  <!-- Slide 2: summary -->
  <svg class="slide slide--summary" viewBox="0 0 904 677" xmlns="http://www.w3.org/2000/svg" aria-label="SOC Performance Improvement Objectives summary">
    <line class="hairline" x1="0" y1="321" x2="904" y2="321"/>
    <polygon class="band" points="0,0 388,0 412,27 904,27 904,97 0,97"/>
    <text class="slide-title" x="44" y="80">SOC Performance Improvement Objectives…</text>

    <text class="headline"><tspan x="452" y="166">Reduce  <tspan class="accent">Incidents</tspan>, Respond <tspan class="accent">Faster</tspan></tspan><tspan x="452" y="201">with Fewer <tspan class="accent">Resources</tspan></tspan></text>

    <circle class="hub--navy" cx="452" cy="366" r="110"/>
    <text class="hub-text"><tspan x="452" y="347">Reduce Total</tspan><tspan x="452" y="380">Cost of</tspan><tspan x="452" y="413">Operations</tspan></text>

    <text class="headline" x="452" y="579">Proactive, Predictive and Preventative</text>

    <polygon class="band" points="617,617 904,617 904,677 0,677 0,660 580,660"/>
    <text class="brand-name" x="864" y="661" text-anchor="end">Stellavant</text>
  </svg>

</main>
</body>
</html>
```